promotional flyer for Valtera Gym

we are after a double sided a5 leaflet to promote our gym, this is to go out to the general public to entice them into getting membership.

gym membership is £30 per month

it should also include the offer of - if you present this leaflet then there will be no joining fee

some of the features of the gym include

strength machines
cardio machines
functional area
sprung floor mat area

Target Market(s)

Adults 16+ who want to go to the gym and workout

Industry/Entity Type

Gym

Font styles to use
Other font styles liked:
• montserrat Regular

Requirements
Must have
• Clean on brand design
• use images supplied by us
Nice to have
• focus on an inclusive experience as the gym will be advertised to everyone
• should also use our "fitter, stronger, Healthier"

```html
<!DOCTYPE html>
<html lang="en">
<head>
<meta charset="utf-8">
<title>Valtera Gym – Membership Flyer</title>
<link href="https://fonts.googleapis.com/css2?family=Montserrat:ital,wght@0,400;0,500;0,600;0,700;0,800;1,700;1,800&display=swap" rel="stylesheet">
<style>
  :root{
    --backdrop:#b02c05;
    --brand-orange:#e2572b;
    --brand-orange-soft:#ea6a43;
    --ink:#2b2b2b;
    --ink-soft:#555555;
    --paper:#f4f4f4;
    --white:#ffffff;
    --shadow-grey:#8a8a8a;
  }
  html,body{margin:0;padding:0;width:1200px;height:1200px;overflow:hidden;background:var(--backdrop);}
  body{font-family:"Montserrat",sans-serif;position:relative;}
  .flyer{position:absolute;left:204px;top:40px;width:792px;height:1120px;background:var(--paper);overflow:hidden;}
  .flyer__shapes{position:absolute;inset:0;}
  .brand{position:absolute;left:0;top:14px;width:240px;text-align:center;}
  .brand__mark{width:40px;height:40px;border-radius:50%;background:var(--brand-orange);margin:0 auto 8px;}
  .brand__name{font-size:21px;font-weight:500;letter-spacing:1px;color:var(--ink);line-height:1;}
  .price-badge{position:absolute;left:500px;top:310px;width:224px;height:224px;border-radius:50%;background:var(--brand-orange);
    border:20px solid var(--white);box-sizing:content-box;margin:-20px 0 0 -20px;display:flex;flex-direction:column;align-items:center;justify-content:center;color:var(--white);}
  .price-badge__amount{font-size:54px;font-weight:800;line-height:1;letter-spacing:-1px;}
  .price-badge__amount small{font-size:19px;font-weight:800;letter-spacing:0;vertical-align:14px;margin-left:2px;}
  .price-badge__label{font-size:16px;font-weight:800;font-style:italic;margin-top:8px;letter-spacing:.3px;}
  .offer{position:absolute;left:56px;top:574px;margin:0;font-weight:700;}
  .offer__line{display:inline-block;background:var(--white);color:var(--brand-orange);font-size:52px;font-weight:700;line-height:56px;
    padding:0 22px 0 10px;margin-bottom:12px;box-shadow:4px 4px 0 var(--shadow-grey);white-space:nowrap;}
  .offer__row{display:block;}
  .call{position:absolute;left:0;top:866px;width:366px;height:80px;background:var(--brand-orange);border-radius:0 40px 40px 0;color:var(--white);}
  .call__label{position:absolute;left:60px;top:10px;font-size:15px;font-weight:400;}
  .call__number{position:absolute;left:60px;top:32px;font-size:32px;font-weight:600;letter-spacing:1.5px;}
  .facility{position:absolute;left:494px;top:822px;}
  .facility__title{font-size:25px;font-weight:700;color:var(--ink);margin:0 0 10px 4px;}
  .facility__list{list-style:none;margin:0;padding:0;}
  .facility__item{position:relative;padding-left:40px;font-size:18px;font-weight:500;color:var(--ink-soft);height:39px;line-height:26px;}
  .facility__item::before{content:"";position:absolute;left:0;top:5px;width:17px;height:17px;border-radius:50%;background:var(--brand-orange-soft);}
  .footer-rule{position:absolute;left:0;right:0;top:1064px;height:2px;background:var(--brand-orange-soft);}
  .footer__web{position:absolute;left:50px;top:1082px;font-size:14px;letter-spacing:3px;color:var(--ink);}
  .footer__social{position:absolute;right:44px;top:1078px;display:flex;align-items:center;gap:12px;font-size:16px;font-weight:600;color:var(--ink);}
  .footer__social-mark{width:26px;height:26px;border-radius:5px;background:var(--brand-orange-soft);}
</style>
</head>
<body>
<main class="flyer">
  <svg class="flyer__shapes" width="792" height="1120" viewBox="0 0 792 1120">
    <defs>
      <linearGradient id="top-photo-tone" x1="0" y1="0" x2="1" y2="1">
        <stop offset="0" stop-color="#c9c9cc"/>
        <stop offset=".35" stop-color="#4a4d55"/>
        <stop offset=".75" stop-color="#3a3c44"/>
        <stop offset="1" stop-color="#6a4238"/>
      </linearGradient>
      <linearGradient id="bottom-photo-tone" x1="0" y1="0" x2="1" y2="1">
        <stop offset="0" stop-color="#e3d6d2"/>
        <stop offset=".5" stop-color="#ececec"/>
        <stop offset="1" stop-color="#f3f3f3"/>
      </linearGradient>
    </defs>
    <rect class="orange-band" x="0" y="0" width="792" height="1120" fill="var(--brand-orange)"/>
    <path role="img" aria-label="Photo of two women smiling on spin bikes in the gym" d="M0 0 H792 V194 C700 300 560 390 426 394 C280 398 140 330 0 266 Z" fill="url(#top-photo-tone)"/>
    <path role="img" aria-label="Faded photo of a member training on a strength machine" d="M0 554 C110 480 260 446 400 446 C560 446 700 470 792 482 V1120 H0 Z" fill="url(#bottom-photo-tone)"/>
  </svg>

  <header class="brand">
    <div class="brand__mark"></div>
    <div class="brand__name">VALTERA GYM</div>
  </header>

  <div class="price-badge">
    <div class="price-badge__amount">£30<small>/month</small></div>
    <div class="price-badge__label">GYM MEMBERSHIP</div>
  </div>

  <h1 class="offer">
    <span class="offer__row"><span class="offer__line">TAKE THIS</span></span>
    <span class="offer__row"><span class="offer__line">LEAFLET FOR</span></span>
    <span class="offer__row"><span class="offer__line">FREE JOINING</span></span>
  </h1>

  <div class="call">
    <div class="call__label">CALL US</div>
    <div class="call__number">+0000000000</div>
  </div>

  <section class="facility">
    <h2 class="facility__title">Facility</h2>
    <ul class="facility__list">
      <li class="facility__item">Strength Machines</li>
      <li class="facility__item">Cardio Machines</li>
      <li class="facility__item">Functional Area</li>
      <li class="facility__item">Sprung Floormat Area</li>
    </ul>
  </section>

  <div class="footer-rule"></div>
  <div class="footer__web">www.valteragym.co.uk</div>
  <div class="footer__social"><span class="footer__social-mark"></span>valteragymuk</div>
</main>
</body>
</html>
```